" Somos uma escola de Yoga e oferecemos aulas, Cursos de Formaçao para Professores de Yoga, workshops e retiros de meditaçao pelo Brasil e em países como Costa Rica, Panamá, Bali e Tailandia. Trabalhamos com o metodo Yin e Yang.. onde yin é a energia da meditaçao, contemplaçao e observaçao e yang do movimento, rítmo, força e atividade. "

```html
<!DOCTYPE html>
<html lang="pt-BR">
<head>
<meta charset="utf-8">
<title>Casa Aurora – Pasta</title>
<link rel="stylesheet" href="https://fonts.googleapis.com/css2?family=Montserrat:wght@400;600&display=swap">
<style>
  :root {
    --green: #8cc63f;
    --green-dark: #7ab32f;
    --ink: #2b2b2b;
    --white: #ffffff;
    --backdrop: #ecebe8;
  }
  html, body {
    margin: 0;
    width: 1200px;
    height: 1200px;
    overflow: hidden;
    background: var(--backdrop);
  }
  .folder {
    display: block;
    width: 1200px;
    height: 1200px;
  }
  .panel-green { fill: var(--green); }
  .pocket { fill: var(--green-dark); }
  .panel-white { fill: var(--white); }
  .brand-name {
    font-family: "Montserrat", sans-serif;
    font-weight: 400;
    font-size: 38px;
    fill: var(--ink);
  }
  .brand-tag {
    font-family: "Montserrat", sans-serif;
    font-weight: 600;
    font-size: 13px;
    letter-spacing: 2px;
    fill: var(--green-dark);
  }
  .brand-dot { fill: var(--green); }
  .contact-text {
    font-family: "Montserrat", sans-serif;
    font-size: 10px;
    fill: var(--white);
  }
  .contact-icon { fill: var(--white); }
</style>
</head>
<body>
<svg class="folder" viewBox="0 0 1200 1200" xmlns="http://www.w3.org/2000/svg">
  <defs>
    <radialGradient id="emblemGlow" cx="50%" cy="50%" r="50%">
      <stop offset="0%" stop-color="#a6d862" stop-opacity="0.55"/>
      <stop offset="100%" stop-color="#a6d862" stop-opacity="0"/>
    </radialGradient>
    <filter id="softShadow" x="-10%" y="-10%" width="120%" height="120%">
      <feDropShadow dx="0" dy="6" stdDeviation="10" flood-opacity="0.18"/>
    </filter>
  </defs>

  <g class="side-tabs">
    <path class="panel-green" d="M200 540 L160 560 L160 610 L200 620 Z"/>
    <path class="pocket" d="M200 625 L165 640 L165 690 L200 700 Z"/>
  </g>

  <g filter="url(#softShadow)">
    <rect class="panel-green" x="200" y="200" width="400" height="640"/>
    <rect class="panel-white" x="600" y="200" width="420" height="640"/>
  </g>

  <circle role="img" aria-label="Faint circular ornament in light green" cx="380" cy="460" r="190" fill="url(#emblemGlow)"/>

  <g class="contacts">
    <rect class="contact-icon" x="215" y="583" width="7" height="7" rx="1"/>
    <text class="contact-text" x="228" y="590">+55 11 4000-1234</text>
    <rect class="contact-icon" x="215" y="598" width="7" height="7" rx="1"/>
    <text class="contact-text" x="228" y="605">+55 11 4000-5678</text>
    <rect class="contact-icon" x="215" y="613" width="7" height="7" rx="1"/>
    <text class="contact-text" x="228" y="620">R. das Flores, 120 - SP</text>
    <rect class="contact-icon" x="215" y="628" width="7" height="7" rx="1"/>
    <text class="contact-text" x="228" y="635">contato@casaaurora.com.br</text>
    <rect class="contact-icon" x="215" y="643" width="7" height="7" rx="1"/>
    <text class="contact-text" x="228" y="650">www.casaaurora.com.br</text>
  </g>

  <path class="pocket" d="M200 700 L560 700 Q650 700 660 780 L668 840 L200 840 Z"/>

  <g class="brand">
    <circle class="brand-dot" cx="810" cy="440" r="34"/>
    <text class="brand-name" x="810" y="520" text-anchor="middle">Casa Aurora</text>
    <text class="brand-tag" x="810" y="546" text-anchor="middle">escola de yoga</text>
  </g>
</svg>
</body>
</html>
```